Professional Law Firm Rebranding Brochure Layout Design

Our law firm is changing its name from The Law Office of Dana Moreno, PLLC to MORENO.LAW. I would like a 4-page color brochure (cover, page 2, page 3, back) that announces and explains our rebranding. I have attached lots of files that should be helpful. I envision the words "The Law Office of Dana Moreno, PLLC is now known as MORENO.LAW" at the top of the front cover. Feel free to review our website at https://moreno-legal.example to get an idea of the look and feel we like. Tall buildings and other professional images work well.

Target Market(s)

Businesses, law firm clients, entrepreneurs, startups, corporations

Industry/Entity Type

Legal

Font styles to use
Sans Serif

Colors
cfdeed
85abd2
3276b5
0555a3
cee9f5
85cae6
33a6d7
0492cd

Requirements
Must have
• Professional appearance, photos & bios of team members, explanation of rebranding - finished product is US letter size

```html
<!DOCTYPE html>
<html lang="en">
<head>
<meta charset="utf-8">
<title>MORENO.LAW Rebranding Brochure Spread</title>
<link href="https://fonts.googleapis.com/css2?family=Bebas+Neue&family=Lato:wght@400;700&family=Montserrat:wght@700&display=swap" rel="stylesheet">
<style>
  :root {
    --charcoal: #3f3f41;
    --brand-blue: #0555a3;
    --paper: #ffffff;
    --canvas: #ececec;
    --ink: #4a4a4a;
    --rule: #9a9a9a;
  }
  * { box-sizing: border-box; margin: 0; padding: 0; }
  html, body { width: 880px; height: 1200px; overflow: hidden; }
  body {
    background: var(--canvas);
    font-family: "Lato", Arial, sans-serif;
    position: relative;
  }
  .spread {
    position: absolute;
    left: 28px; top: 306px;
    width: 824px; height: 588px;
    background: var(--paper);
    box-shadow: 0 8px 20px rgba(0,0,0,.18);
    overflow: hidden;
  }
  .inside-panel {
    position: absolute; left: 0; top: 0;
    width: 277px; height: 461px;
    background: var(--charcoal);
    color: var(--paper);
    padding: 46px 20px 0 19px;
  }
  .inside-panel p {
    font-size: 9.2px; line-height: 1.26;
    text-align: justify; margin-bottom: 11px;
  }
  .inside-panel p.invitation {
    font-size: 12px; line-height: 1.3; margin-top: 4px;
  }
  .invitation strong { font-weight: 700; white-space: nowrap; }
  .cityscape {
    position: absolute; left: 277px; top: 0;
    width: 547px; height: 461px;
  }
  .cover-headline {
    position: absolute; right: 28px; top: 40px;
    text-align: right; color: var(--paper);
  }
  .headline-main {
    font-family: "Bebas Neue", Impact, sans-serif;
    font-size: 60px; line-height: .95; letter-spacing: .5px;
  }
  .headline-sub {
    font-family: "Montserrat", Arial, sans-serif;
    font-weight: 700; font-size: 26px; line-height: 1.3;
  }
  .headline-name {
    font-family: "Bebas Neue", Impact, sans-serif;
    font-size: 70px; line-height: 1; margin-top: 4px;
  }
  .brand-rule {
    position: absolute; left: 0; top: 461px;
    width: 824px; height: 4px; background: var(--brand-blue);
  }
  .fold-shadow {
    position: absolute; left: 402px; top: 0;
    width: 20px; height: 588px;
    background: linear-gradient(90deg, rgba(0,0,0,0) 0%, rgba(0,0,0,.08) 50%, rgba(0,0,0,0) 100%);
  }
  .office {
    position: absolute; top: 490px;
    font-size: 13px; line-height: 1.4; color: var(--ink);
    font-style: normal;
  }
  .office h3 {
    font-size: 13.5px; font-weight: 700; color: var(--brand-blue);
    text-transform: uppercase;
  }
  .office-primary { left: 21px; }
  .office-secondary { left: 249px; }
  .office-divider {
    position: absolute; left: 230px; top: 490px;
    width: 1px; height: 55px; background: var(--rule);
  }
  .brand-lockup {
    position: absolute; left: 492px; top: 502px;
    display: flex; align-items: center; gap: 12px;
  }
  .brand-dot {
    width: 28px; height: 28px; border-radius: 50%;
    background: var(--brand-blue);
  }
  .brand-name {
    font-family: "Lato", Arial, sans-serif;
    font-weight: 700; font-size: 32px; line-height: 1;
    color: var(--brand-blue);
  }
</style>
</head>
<body>
  <main class="spread">
    <section class="inside-panel">
      <p>At MORENO.LAW, we strive to help our clients avoid costly legal mistakes. Preventing legal problems is always cheaper and easier than dealing with them after they occur, which is why our attorneys and staff pride themselves on anticipating clients' needs and meeting them.</p>
      <p>Our primary areas of practice are business and intellectual property law. Our firm's clients range from entrepreneurs and startup companies to multi-national corporations. We understand that regardless of where your company may be in its life cycle, legal decisions are business decisions. Your strategic business objectives always factor into our legal advice.</p>
      <p>MORENO.LAW's goal is to enrich and empower our clients by providing high quality work product and creative legal solutions to their legal problems. One way we achieve this goal is by leveraging technology and utilizing data to improve the efficiency and effectiveness of our services.</p>
      <p class="invitation">We would welcome the opportunity to earn a place as your reliable trusted advisor. To learn more about MORENO.LAW, please contact us at <strong>info@moreno-legal.example</strong> <strong>or 555-014-2290</strong></p>
    </section>

    <svg class="cityscape" viewBox="0 0 547 461" role="img" aria-label="Photograph of glass skyscrapers rising into a bright blue sky with soft clouds">
      <defs>
        <linearGradient id="sky" x1="0" y1="0" x2="0" y2="1">
          <stop offset="0" stop-color="#0d5eab"/>
          <stop offset=".45" stop-color="#3276b5"/>
          <stop offset=".75" stop-color="#85abd2"/>
          <stop offset="1" stop-color="#cfdeed"/>
        </linearGradient>
      </defs>
      <rect width="547" height="461" fill="url(#sky)"/>
    </svg>

    <header class="cover-headline">
      <div class="headline-main">THE LAW OFFICE</div>
      <div class="headline-sub">of Dana Moreno PLLC</div>
      <div class="headline-sub">is now known as</div>
      <div class="headline-name">MORENO.LAW</div>
    </header>

    <div class="brand-rule"></div>
    <div class="fold-shadow"></div>

    <address class="office office-primary">
      <h3>Riverton Office</h3>
      418 Harbor Lane,<br>Suite 200, Riverton, NC 28000
    </address>
    <div class="office-divider"></div>
    <address class="office office-secondary">
      <h3>Maple Hill Office</h3>
      75 Orchard Row<br>Maple Hill, NC 28001
    </address>

    <div class="brand-lockup">
      <div class="brand-dot"></div>
      <div class="brand-name">MORENO.LAW</div>
    </div>
  </main>
</body>
</html>
```